FinTech company looking to revamp and expand client-facing interface for our financial models

Halvern Ledgerworks currently has a very simple website that allows clients to interact with our financial models. We are looking to completely redesign the current site and add several extra pages to provide extra functionality. We want the design to have a modern, slick feel, that will work on both a desktop or a tablet. It should be straightforward for clients to move between different pages at any time, and clear from the layout how to interact with the more advanced features. We have included screenshots of existing pages in the attached design brief, as well as sketches of the functionality required by the new pages, but can't provide a direct link to the current site.
Target Market(s)
Professional investors that will be paying to access the interface
Industry/Entity Type
Finance
Number of Pages Required
4 page
Colors
Designer to choose colors to be used in the design.
Look and feel
Each slider illustrates characteristics of the customer's brand and the style your logo design should communicate.

```html
<!DOCTYPE html>
<html lang="en">
<head>
<meta charset="utf-8">
<title>Halvern Ledgerworks · KESTREL</title>
<link href="https://fonts.googleapis.com/css2?family=Roboto:wght@400;500;700&display=swap" rel="stylesheet">
<style>
  :root {
    --navy: #0b1b2b;
    --purple: #4a2db5;
    --purple-dark: #2b1777;
    --ink: #0f1a28;
    --muted: #6f7780;
    --head: #a89cdb;
    --row-alt: #f7f7f8;
    --line: #d3d6da;
    --nav-text: #a9b1ba;
  }
  * { box-sizing: border-box; margin: 0; padding: 0; }
  html, body { width: 1200px; height: 1042px; overflow: hidden; background: #fff; }
  body { font-family: "Roboto", Arial, sans-serif; color: var(--ink); position: relative; }

  .site-header { height: 83px; background: var(--navy); position: relative; }
  .brand { position: absolute; left: 112px; top: 34px; color: #fff; font-size: 13px; font-weight: 500; letter-spacing: 4.6px; text-transform: uppercase; }
  .main-nav { position: absolute; right: 116px; top: 35px; display: flex; gap: 24px; font-size: 11.5px; color: var(--nav-text); }
  .main-nav span { display: flex; align-items: center; gap: 4px; }

  .crumb-bar { height: 37px; background: var(--purple); position: relative; color: #fff; font-size: 11.5px; }
  .crumbs { position: absolute; left: 111px; top: 0; height: 37px; display: flex; align-items: center; gap: 10px; }
  .periods { position: absolute; left: 950px; top: 0; display: flex; height: 37px; }
  .periods span { display: flex; align-items: center; padding: 0 10px; }
  .periods .active { background: var(--purple-dark); }

  .filters { position: absolute; top: 153px; left: 112px; width: 976px; height: 92px; }
  .field { position: absolute; top: 0; width: 309px; }
  .field-label { font-size: 11.5px; font-weight: 500; }
  .field-label sup { font-size: 6px; }
  .field-sub { font-size: 11.5px; color: var(--muted); margin-top: 3px; }
  .field-input { position: absolute; top: 42px; width: 309px; height: 50px; background: #fff; box-shadow: 0 6px 18px rgba(20,30,50,.09); font-size: 11.5px; padding-left: 17px; line-height: 50px; }
  .filter-btn { position: absolute; left: 667px; top: 42px; width: 309px; height: 50px; background: var(--purple); color: #fff; font-size: 11.5px; font-weight: 500; display: flex; align-items: center; justify-content: center; border-radius: 2px; box-shadow: 0 6px 18px rgba(74,45,181,.2); }

  .section-title { position: absolute; left: 112px; top: 340px; font-size: 24px; font-weight: 500; display: flex; align-items: center; gap: 10px; }
  .export-btn { position: absolute; left: 1000px; top: 337px; width: 88px; height: 34px; border: 1px solid var(--purple); border-radius: 2px; color: var(--purple); font-size: 11.5px; font-weight: 500; display: flex; align-items: center; justify-content: center; }

  .data-card { position: absolute; left: 112px; top: 389px; width: 976px; height: 493px; background: #fff; box-shadow: 0 6px 22px rgba(20,30,50,.08); padding-top: 24px; }
  .row { display: grid; grid-template-columns: 29px 83px 142px 91px 79px 65px 66px 66px 67px 66px 66px 65px 1fr; padding-left: 26px; height: 43.3px; align-items: center; font-size: 11.5px; color: var(--muted); }
  .row.head { color: var(--head); height: 21px; margin-bottom: 14px; }
  .row.head .sorted { color: var(--purple); font-weight: 500; }
  .row:nth-child(odd):not(.head) { background: var(--row-alt); }
  .check { width: 11px; height: 11px; border: 1px solid var(--line); border-radius: 1px; }
  .caret { display: inline-block; margin-left: 3px; vertical-align: middle; }
</style>
</head>
<body>
  <header class="site-header">
    <div class="brand">Halvern Ledgerworks</div>
    <nav class="main-nav">
      <span><svg width="9" height="8" viewBox="0 0 9 8"><rect x="0" y="4" width="1.5" height="4" fill="#a9b1ba"/><rect x="2.5" y="2" width="1.5" height="6" fill="#a9b1ba"/><rect x="5" y="0" width="1.5" height="8" fill="#a9b1ba"/><rect x="7.5" y="3" width="1.5" height="5" fill="#a9b1ba"/></svg>Models<svg class="caret" width="6" height="4" viewBox="0 0 6 4"><path d="M0 0h6L3 3z" fill="#a9b1ba"/></svg></span>
      <span><svg width="8" height="8" viewBox="0 0 8 8"><circle cx="4" cy="4" r="2.5" fill="none" stroke="#a9b1ba" stroke-width="1.2" stroke-dasharray="1.5 1"/></svg>Sensitivities</span>
      <span><svg width="9" height="9" viewBox="0 0 10 10"><path d="M5 0l1.5 3.2 3.5.4-2.6 2.4.7 3.5L5 7.8 1.9 9.5l.7-3.5L0 3.6l3.5-.4z" fill="#a9b1ba"/></svg>Favourites</span>
    </nav>
  </header>

  <div class="crumb-bar">
    <div class="crumbs"><span>Home</span><svg width="5" height="7" viewBox="0 0 5 7"><path d="M1 1l2.5 2.5L1 6" fill="none" stroke="#fff" stroke-width="1"/></svg><span>KESTREL</span></div>
    <div class="periods"><span class="active">250D</span><span>83D</span><span>42D</span></div>
  </div>

  <section class="filters">
    <div class="field" style="left:0">
      <div class="field-label">Quality</div>
      <div class="field-sub">Threshold</div>
    </div>
    <div class="field-input" style="left:0">-10</div>
    <div class="field" style="left:334px">
      <div class="field-label">ABS <sup>Stat</sup></div>
      <div class="field-sub">Threshold</div>
    </div>
    <div class="field-input" style="left:334px">-10</div>
    <div class="filter-btn">Filter</div>
  </section>

  <h1 class="section-title">KESTREL
    <svg width="15" height="15" viewBox="0 0 15 15"><circle cx="6" cy="6" r="4.3" fill="none" stroke="#4a2db5" stroke-width="2"/><path d="M9.2 9.2l4.3 4.3" stroke="#4a2db5" stroke-width="2.4" stroke-linecap="round"/></svg>
  </h1>
  <div class="export-btn">Export</div>

  <main class="data-card">
    <div class="row head">
      <div class="check"></div>
      <div class="sorted">ID<svg class="caret" width="6" height="4" viewBox="0 0 6 4"><path d="M0 0h6L3 3z" fill="#4a2db5"/></svg></div>
      <div>Sector<svg class="caret" width="6" height="4" viewBox="0 0 6 4"><path d="M0 0h6L3 3z" fill="#a89cdb"/></svg></div>
      <div>Time<svg class="caret" width="6" height="4" viewBox="0 0 6 4"><path d="M0 3h6L3 0z" fill="#a89cdb"/></svg></div>
      <div>Quality</div><div>Stat 1</div><div>Stat 2</div><div>Stat 3</div><div>Stat 4</div><div>Stat 5</div><div>Stat 6</div><div>Stat 7</div><div>Stat 8</div>
    </div>
    <div class="row"><div class="check"></div><div>Model 1</div><div>Materials</div><div>Jun 19 2019</div><div>95,226</div><div>22,373</div><div>66,838</div><div>29,472</div><div>52,683</div><div>36,407</div><div>82,672</div><div>18,491</div><div>66,425</div></div>
    <div class="row"><div class="check"></div><div>Model 1234</div><div>Consumer Discretionary</div><div>Jun 19 2019</div><div>95,226</div><div>22,373</div><div>66,838</div><div>29,472</div><div>52,683</div><div>36,407</div><div>82,672</div><div>18,491</div><div>66,425</div></div>
    <div class="row"><div class="check"></div><div>Model 1</div><div>Materials</div><div>Jun 19 2019</div><div>95,226</div><div>22,373</div><div>66,838</div><div>29,472</div><div>52,683</div><div>36,407</div><div>82,672</div><div>18,491</div><div>66,425</div></div>
    <div class="row"><div class="check"></div><div>Model Name</div><div>Materials</div><div>Jun 19 2019</div><div>95,226</div><div>22,373</div><div>66,838</div><div>29,472</div><div>52,683</div><div>36,407</div><div>82,672</div><div>18,491</div><div>66,425</div></div>
    <div class="row"><div class="check"></div><div>Model 1</div><div>Materials</div><div>Jun 19 2019</div><div>95,226</div><div>22,373</div><div>66,838</div><div>29,472</div><div>52,683</div><div>36,407</div><div>82,672</div><div>18,491</div><div>66,425</div></div>
    <div class="row"><div class="check"></div><div>Model 1</div><div>Materials</div><div>Jun 19 2019</div><div>95,226</div><div>22,373</div><div>66,838</div><div>29,472</div><div>52,683</div><div>36,407</div><div>82,672</div><div>18,491</div><div>66,425</div></div>
    <div class="row"><div class="check"></div><div>Model 1</div><div>Materials</div><div>Jun 19 2019</div><div>95,226</div><div>22,373</div><div>66,838</div><div>29,472</div><div>52,683</div><div>36,407</div><div>82,672</div><div>18,491</div><div>66,425</div></div>
    <div class="row"><div class="check"></div><div>Model 1</div><div>Materials</div><div>Jun 19 2019</div><div>95,226</div><div>22,373</div><div>66,838</div><div>29,472</div><div>52,683</div><div>36,407</div><div>82,672</div><div>18,491</div><div>66,425</div></div>
    <div class="row"><div class="check"></div><div>Model 1</div><div>Materials</div><div>Jun 19 2019</div><div>95,226</div><div>22,373</div><div>66,838</div><div>29,472</div><div>52,683</div><div>36,407</div><div>82,672</div><div>18,491</div><div>66,425</div></div>
    <div class="row"><div class="check"></div><div>Model 1</div><div>Materials</div><div>Jun 19 2019</div><div>95,226</div><div>22,373</div><div>66,838</div><div>29,472</div><div>52,683</div><div>36,407</div><div>82,672</div><div>18,491</div><div>66,425</div></div>
  </main>
</body>
</html>
```